3 Page Design for Northbrook Capital

We want a Home Page, About Page, and Products & Services Page for Northbrook Capital. Please refer to the attached docs for more info.
If done in Figma, would like Figma files that can easily be ported to Wordpress.

```html
<!DOCTYPE html>
<html lang="en">
<head>
<meta charset="utf-8">
<title>Northbrook Capital — Home</title>
<link href="https://fonts.googleapis.com/css2?family=Inter:wght@400;500;600;700&family=Roboto+Condensed:wght@400;500;700&display=swap" rel="stylesheet">
<style>
:root{
  --ink:#2b2b2b;
  --text:#444;
  --muted:#666;
  --red:#9b1b30;
  --grey:#9d9d9d;
  --violet:#6b5a99;
  --soft:#f3f3f3;
  --footer:#2d2d2d;
  --white:#fff;
}
*{box-sizing:border-box;margin:0;padding:0}
html,body{width:1200px;height:3538px;overflow:hidden;background:var(--white)}
body{position:relative;font-family:"Inter",Arial,sans-serif;color:var(--ink)}
.abs{position:absolute}

/* header */
.site-header{position:absolute;left:0;top:0;width:1200px;height:77px;background:var(--white);z-index:2}
.brand{position:absolute;left:125px;top:0;width:210px;height:115px;background:var(--white);display:flex;flex-direction:column;align-items:center;justify-content:center;gap:8px}
.brand-dot{width:40px;height:40px;border-radius:50%;background:var(--ink)}
.brand-name{font-weight:700;font-size:16px;color:var(--ink);letter-spacing:.2px}
.nav a{position:absolute;top:16px;height:44px;line-height:44px;font-size:16px;color:var(--ink);text-decoration:none}
.nav .active{left:590px;width:72px;background:var(--red);color:var(--white);text-align:center}

/* hero */
.hero{position:absolute;left:0;top:77px;width:1200px;height:599px;background:linear-gradient(90deg,#e8e9ef 0%,#dcdde5 45%,#b9bcc6 70%,#8e929c 100%)}
.hero-photo{position:absolute;left:600px;top:0;width:600px;height:599px;background:linear-gradient(160deg,#c9ccd4 0%,#8a8e98 60%,#5d616b 100%)}
.hero h1{position:absolute;left:144px;top:147px;font-size:50px;line-height:56px;font-weight:700;color:var(--ink);letter-spacing:-.5px}
.hero p{position:absolute;left:144px;top:265px;width:440px;font-size:14.5px;line-height:24px;color:var(--muted)}
.btn{position:absolute;background:var(--red);color:var(--white);font-weight:600;font-size:14px;display:flex;align-items:center;justify-content:center;border-radius:3px;text-decoration:none}
.hero .btn{left:144px;top:346px;width:207px;height:52px}
.arrow{position:absolute;top:487px;width:40px;height:40px;border-radius:50%;background:var(--white);display:flex;align-items:center;justify-content:center;box-shadow:0 1px 4px rgba(0,0,0,.15)}

/* advantage */
.advantage{position:absolute;left:0;top:676px;width:1200px;height:508px;background:var(--soft)}
.section-title{position:absolute;left:0;width:1200px;text-align:center;font-weight:700;color:var(--ink);letter-spacing:-.5px}
.advantage .section-title{top:90px;font-size:49px}
.advantage .lead{position:absolute;left:270px;top:160px;width:660px;text-align:center;font-size:14.5px;line-height:24px;color:var(--text)}
.value-card{position:absolute;top:227px;width:217px;height:160px;border-radius:6px;display:flex;flex-direction:column;align-items:center;justify-content:center;gap:12px;color:var(--white);font-weight:600;font-size:19px}
.value-card.dark{left:144px;background:#2d2d2d}
.value-card.grey{left:375px;background:var(--grey)}
.value-card.red{left:607px;background:var(--red)}
.value-card.violet{left:838px;background:var(--violet)}

/* story */
.story-mark{position:absolute;left:176px;top:1318px;width:373px;height:384px;display:flex;flex-direction:column;align-items:center;justify-content:center;gap:20px}
.story-mark .ring{width:250px;height:250px;border-radius:50%;border:34px solid #d9d2c4}
.story-mark .name{font-size:26px;font-weight:700;color:var(--ink)}
.story h2{position:absolute;left:611px;top:1286px;font-size:48px;font-weight:700;letter-spacing:-.5px}
.story p{position:absolute;left:614px;width:436px;font-size:14.5px;line-height:24px;color:var(--text)}
.story .btn{left:611px;top:1659px;width:180px;height:51px}

/* offers */
.offers .section-title{top:1820px;font-size:48px}
.offer-img{position:absolute;border-radius:4px}
.offer-label{position:absolute;text-align:center;font-size:19.5px;font-weight:600;color:var(--ink)}

/* cta */
.cta .section-title{top:2836px;font-size:48px;line-height:56px}
.cta .btn{left:490px;top:2967px;width:220px;height:51px}

/* footer */
.site-footer{position:absolute;left:0;top:3143px;width:1200px;height:395px;background:var(--footer);color:var(--white);font-family:"Roboto Condensed",Arial,sans-serif}
.site-footer h3{position:absolute;top:70px;font-family:"Inter",Arial,sans-serif;font-size:19px;line-height:28px;font-weight:600;text-transform:uppercase}
.newsletter-input{position:absolute;left:143px;top:136px;width:270px;height:41px;border:1px solid #888;display:flex;align-items:center;justify-content:space-between;padding:0 16px;font-size:13px;color:#ddd}
.social{position:absolute;top:199px;width:28px;height:28px;border-radius:50%;background:#444}
.social.on{background:var(--white)}
.contact-item .label{position:absolute;left:546px;font-weight:700;font-size:15px}
.contact-item .value{position:absolute;left:546px;font-size:13px;color:#ddd}
.contact-icon{position:absolute;left:505px}
.quick a{position:absolute;color:var(--white);text-decoration:none;font-size:15.5px;padding-left:24px}
.quick a::before{content:"»";position:absolute;left:0;top:-2px;font-size:17px}
.copyright{position:absolute;left:0;top:344px;width:1200px;text-align:center;font-size:15px;color:#e6e6e6;font-family:"Inter",Arial,sans-serif}
</style>
</head>
<body>

<header class="site-header">
  <div class="brand">
    <span class="brand-dot"></span>
    <span class="brand-name">Northbrook Capital</span>
  </div>
  <nav class="nav">
    <a class="active" href="#">Home</a>
    <a href="#" style="left:692px">About</a>
    <a href="#" style="left:778px">Products &amp; Services</a>
    <a href="#" style="left:972px">Contact Us</a>
  </nav>
</header>

<section class="hero">
  <div class="hero-photo" role="img" aria-label="Photo of a senior businessman in a suit seated in a grey armchair by a bright window"></div>
  <h1>Where Discipline<br>Meets Wealth.</h1>
  <p>Guiding athletes, professionals, and high-performers into their next chapter — the stage where preparation, strategy, and smart decisions create generational success.</p>
  <a class="btn" href="#">Explore Our Services</a>
  <span class="arrow" style="left:144px"><svg width="14" height="14" viewBox="0 0 14 14"><path d="M9 2 4 7l5 5" fill="none" stroke="#222" stroke-width="2"/></svg></span>
  <span class="arrow" style="left:191px"><svg width="14" height="14" viewBox="0 0 14 14"><path d="m5 2 5 5-5 5" fill="none" stroke="#222" stroke-width="2"/></svg></span>
</section>

<section class="advantage">
  <h2 class="section-title">The Northbrook Advantage</h2>
  <p class="lead">Guiding athletes, professionals, and high-performers into their next chapter — the stage where preparation, strategy, and smart decisions create generational success.</p>
  <div class="value-card dark">
    <svg width="54" height="54" viewBox="0 0 54 54"><path d="M27 5a18 18 0 0 0-18 18c0 6 3 10 6 13v13h18v-7h6a4 4 0 0 0 4-4v-8l5-2-5-8A18 18 0 0 0 27 5z" fill="#fff"/><circle cx="27" cy="22" r="7" fill="#2d2d2d"/><circle cx="27" cy="22" r="3" fill="#fff"/></svg>
    Discipline
  </div>
  <div class="value-card grey">
    <svg width="60" height="54" viewBox="0 0 60 54"><path d="M4 28c8-11 16-16 26-16s18 5 26 16c-8 11-16 16-26 16S12 39 4 28z" fill="#fff"/><circle cx="30" cy="28" r="10" fill="#9d9d9d"/><circle cx="30" cy="28" r="5" fill="#fff"/><path d="M30 2v6M14 7l3 5M46 7l-3 5M30 48v5" stroke="#fff" stroke-width="3"/></svg>
    Clarity
  </div>
  <div class="value-card red">
    <svg width="56" height="56" viewBox="0 0 56 56"><rect x="4" y="10" width="22" height="20" fill="#fff"/><rect x="30" y="4" width="22" height="22" fill="#fff"/><rect x="4" y="32" width="22" height="20" fill="#fff"/><rect x="30" y="30" width="22" height="22" fill="#fff" opacity=".85"/><circle cx="28" cy="20" r="4" fill="#fff"/><circle cx="15" cy="31" r="4" fill="#9b1b30"/></svg>
    Integrity
  </div>
  <div class="value-card violet">
    <svg width="60" height="60" viewBox="0 0 60 60"><circle cx="30" cy="30" r="24" fill="none" stroke="#fff" stroke-width="4" stroke-dasharray="60 12"/><circle cx="30" cy="30" r="12" fill="none" stroke="#fff" stroke-width="6" stroke-dasharray="5 3"/><circle cx="30" cy="30" r="5" fill="#fff"/></svg>
    Progress
  </div>
</section>

<section class="story">
  <div class="story-mark">
    <span class="ring"></span>
    <span class="name">Northbrook Capital</span>
  </div>
  <h2>Our Story</h2>
  <p style="top:1351px">Lorem ipsum dolor sit amet, consectetur adipiscing elit, sed do eiusmod tempor incididunt ut labore et dolore magna aliqua. Ut enim ad minim veniam, quis nostrud exercitation ullamco laboris nisi ut aliquip ex ea commodo consequat. Duis aute irure dolor in reprehenderit in voluptate velit esse cillum dolore eu fugiat nulla pariatur. Excepteur sint occaecat cupidatat non proident, sunt in culpa qui officia deserunt mollit anim id est laborum.</p>
  <p style="top:1543px">Lorem ipsum dolor sit amet, consectetur adipiscing elit, sed do eiusmod tempor incididunt ut labore et dolore magna aliqua. Ut enim ad minim veniam, quis nostrud exercitation ullamco laboris nisi ut aliquip ex ea commodo consequat.</p>
  <a class="btn" href="#">Discover More &nbsp;+</a>
</section>

<section class="offers">
  <h2 class="section-title">Offer Framework</h2>
  <div class="offer-img" style="left:14px;top:1908px;width:381px;height:351px;background:linear-gradient(135deg,#c9d2d8,#e6e8ea 50%,#8b8f93)" role="img" aria-label="Photo of a smiling businesswoman shaking hands with a colleague"></div>
  <div class="offer-label" style="left:14px;top:2274px;width:381px">Wealth Planning &amp; Strategy</div>
  <div class="offer-img" style="left:409px;top:1908px;width:382px;height:351px;border:5px solid var(--red);background:linear-gradient(135deg,#3c4654,#9aa3ad 55%,#505560)" role="img" aria-label="Photo of a woman listening to an advisor in a meeting"></div>
  <div class="offer-label" style="left:409px;top:2274px;width:382px">Investment Guidance</div>
  <div class="offer-img" style="left:805px;top:1908px;width:381px;height:351px;background:linear-gradient(135deg,#9a8d6e,#c9b58c 45%,#2b86a8 75%,#7c8a6a)" role="img" aria-label="Photo of a woman jogging outdoors at sunset"></div>
  <div class="offer-label" style="left:805px;top:2274px;width:381px">Career &amp; Transition Support</div>
  <div class="offer-img" style="left:14px;top:2331px;width:575px;height:352px;background:linear-gradient(135deg,#4a6f6a,#b9c3c4 45%,#a8473f 65%,#c9ccd0)" role="img" aria-label="Photo of a team collaborating around a meeting table with laptops"></div>
  <div class="offer-label" style="left:14px;top:2699px;width:575px">Risk Management &amp; Protection</div>
  <div class="offer-img" style="left:611px;top:2331px;width:575px;height:352px;background:linear-gradient(135deg,#2e2e30,#8f8c87 45%,#d8d6d2 65%,#4a4744)" role="img" aria-label="Photo of colleagues discussing business around a laptop in an office"></div>
  <div class="offer-label" style="left:611px;top:2699px;width:575px">Business &amp; Entrepreneurial Guidance</div>
</section>

<section class="cta">
  <h2 class="section-title">Start Planning Your Future<br>With Confidence.</h2>
  <a class="btn" href="#">Book Your Intro Call &nbsp;+</a>
</section>

<footer class="site-footer">
  <h3 style="left:143px">Subscribe to<br>our newsletter</h3>
  <div class="newsletter-input"><span>Email address</span>
    <svg width="14" height="14" viewBox="0 0 14 14"><path d="M13 1 1 6l5 2 2 5z" fill="#fff"/></svg></div>
  <span class="social" style="left:144px"></span>
  <span class="social on" style="left:177px"></span>
  <span class="social" style="left:210px"></span>

  <h3 style="left:504px">Contact info</h3>
  <div class="contact-item">
    <svg class="contact-icon" style="top:123px" width="14" height="18" viewBox="0 0 14 18"><path d="M7 0a7 7 0 0 0-7 7c0 5 7 11 7 11s7-6 7-11a7 7 0 0 0-7-7z" fill="#fff"/><circle cx="7" cy="7" r="2.5" fill="#2d2d2d"/></svg>
    <span class="label" style="top:121px">Address</span>
    <span class="value" style="top:146px">Lorem ipsum dolor sit amet</span>
  </div>
  <div class="contact-item">
    <svg class="contact-icon" style="top:181px" width="20" height="15" viewBox="0 0 20 15"><rect width="20" height="15" rx="1" fill="#fff"/><path d="m1 1 9 7 9-7" fill="none" stroke="#2d2d2d" stroke-width="1.6"/></svg>
    <span class="label" style="top:177px">Email</span>
    <span class="value" style="top:202px">info@companyname.com</span>
  </div>
  <div class="contact-item">
    <svg class="contact-icon" style="top:236px" width="17" height="17" viewBox="0 0 17 17"><path d="M3 0h4l1 4-2 2a11 11 0 0 0 5 5l2-2 4 1v4a2 2 0 0 1-2 2C7 16 1 10 1 2a2 2 0 0 1 2-2z" fill="#fff"/></svg>
    <span class="label" style="top:233px">Phone</span>
    <span class="value" style="top:258px">+1 888 888 8888</span>
  </div>

  <h3 style="left:765px">Quick links</h3>
  <nav class="quick">
    <a href="#" style="left:765px;top:123px">Home</a>
    <a href="#" style="left:765px;top:155px">About</a>
    <a href="#" style="left:765px;top:187px">Services</a>
    <a href="#" style="left:765px;top:219px">Contact</a>
    <a href="#" style="left:901px;top:123px">Terms and Condition</a>
    <a href="#" style="left:901px;top:155px">Privacy policy</a>
    <a href="#" style="left:901px;top:187px">Help</a>
    <a href="#" style="left:901px;top:219px">Support</a>
  </nav>
  <p class="copyright">© Copyrights 2025 | All Rights Reserved</p>
</footer>

</body>
</html>
```